Web design for Money Service Business (uncoded)

We need a very basic website with 5-6 pages. Home page, Services, Transfer(How to use our service), About us, Contact us, FAQ
Our company name is Harbin Coinage. We are a company that deals with currency exchange and international money transfer. We do cash exchange and international money transfers to bank accounts all over the world. We offer highly competitive exchange rates so usually attract customers who transfer money over $10,000. Our niche is with larger sums of money, the design needs to be professional and communicate trust, security and stability.
Industry/Entity Type
Security
Look and feel
Each slider illustrates characteristics of the customer's brand and the style your logo design should communicate.

```html
<!DOCTYPE html>
<html lang="en">
<head>
<meta charset="utf-8">
<title>Harbin Coinage – International Money Transfer</title>
<link rel="stylesheet" href="https://fonts.googleapis.com/css2?family=Roboto:wght@300;400&family=Open+Sans:wght@400;600&family=Tinos:ital@1&display=swap">
<style>
:root{
  --blue:#1d5489;
  --blue-dark:#14416f;
  --orange:#f39c1f;
  --gold:#e3a33a;
  --text:#333;
  --muted:#666;
  --line:#dcdcdc;
  --panel:#ececec;
  --link:#1d5489;
}
*{box-sizing:border-box;margin:0;padding:0}
html,body{width:1120px;height:1200px;overflow:hidden;background:#fff}
body{position:relative;font-family:'Roboto',sans-serif;font-weight:300;color:var(--text)}
a{text-decoration:none;color:inherit}
.topbar{position:absolute;left:0;top:0;width:1120px;height:21px;background:var(--blue)}
.topbar-inner{position:absolute;left:80px;width:960px;height:21px;background:var(--gold);color:#fff;font-size:13px;font-weight:400;display:flex;justify-content:flex-end;align-items:center;gap:16px;padding-right:4px}
.topbar-inner span{display:flex;align-items:center;gap:4px}
.header{position:absolute;left:0;top:21px;width:1120px;height:100px;border-bottom:1px solid var(--line)}
.brand{position:absolute;left:84px;top:22px;display:flex;align-items:center;gap:10px}
.brand-mark{width:34px;height:34px;border-radius:50%;background:var(--blue)}
.brand-name{font-family:'Roboto',sans-serif;font-weight:400;font-size:34px;color:var(--blue);letter-spacing:1px;line-height:1}
.brand-tag{position:absolute;left:84px;top:66px;font-size:13px;letter-spacing:3.2px;color:var(--blue);font-weight:400}
.nav{position:absolute;right:82px;top:43px;display:flex;gap:12px;font-size:14px;color:#555;font-weight:300}
.nav a.active{color:var(--blue);border-bottom:1px solid var(--blue);padding-bottom:2px}
.hero{position:absolute;left:80px;top:145px;width:960px;height:302px;overflow:hidden}
.hero-photo{position:absolute;inset:0;background:linear-gradient(135deg,#c9791b 0%,#f2a43a 35%,#a8621a 70%,#5b3a14 100%)}
.hero-panel{position:absolute;inset:0;background:linear-gradient(120deg,#2a5e94,#173f6c);clip-path:polygon(632px 0,960px 0,960px 302px,642px 302px,540px 151px)}
.hero-edge{position:absolute;inset:0;background:rgba(255,255,255,.55);clip-path:polygon(624px 0,632px 0,540px 151px,642px 302px,634px 302px,532px 151px)}
.hero-copy{position:absolute;left:625px;top:82px;width:320px}
.hero-copy h1{font-weight:400;color:var(--orange);font-size:32px;line-height:29px;letter-spacing:-.5px}
.hero-copy p{color:#fff;font-size:21px;line-height:24px;margin-top:6px}
.intro{position:absolute;left:80px;top:478px;width:707px;font-size:18px;line-height:24px;text-align:justify;color:#333}
.rule{position:absolute;left:78px;top:599px;width:707px;border-top:1px solid var(--line)}
.promo{position:absolute;left:816px;top:480px;width:224px;height:122px;background:var(--orange);overflow:hidden;color:#fff}
.promo-upto{position:absolute;left:40px;top:6px;font-family:'Tinos',serif;font-style:italic;font-size:18px}
.promo-pct{position:absolute;left:16px;top:26px;font-family:'Tinos',serif;font-style:italic;font-size:52px;line-height:1;display:flex}
.promo-pct .stack{display:flex;flex-direction:column;font-size:24px;line-height:20px;margin-left:2px;margin-top:4px}
.promo-label{position:absolute;left:15px;top:82px;font-family:'Open Sans',sans-serif;font-weight:600;font-size:14.5px;line-height:15px}
.promo-globe{position:absolute;left:126px;top:26px;width:75px;height:75px;border-radius:50%;background:#fff}
.promo-corner{position:absolute;right:0;bottom:0;width:84px;height:56px;background:var(--blue-dark);clip-path:polygon(100% 0,100% 100%,0 100%)}
.promo-corner span{position:absolute;right:4px;bottom:10px;font-size:9px;font-weight:400;line-height:10px;transform:rotate(-45deg);text-align:center}
.col{position:absolute;top:632px;width:330px}
.col-who{left:80px}
.col-what{left:460px}
.col-divider{position:absolute;left:438px;top:632px;height:206px;border-left:1px solid var(--line)}
.col-icon{position:absolute;left:0;top:0;width:32px;height:32px}
.col h2{margin-left:40px;font-weight:300;color:var(--orange);font-size:20px;line-height:20px}
.col p{margin-left:42px;font-size:12.5px;line-height:19px;color:var(--muted);text-align:justify;margin-top:6px;width:286px}
.col p+p{margin-top:19px}
.checks{list-style:none;margin-left:39px;margin-top:6px;width:250px}
.checks li{display:flex;align-items:center;gap:7px;font-size:12.8px;color:#444;height:29px;border-bottom:1px dotted #ccc}
.choose{position:absolute;left:80px;top:865px;width:704px;height:160px;border:1px solid #cfcfcf;background:linear-gradient(#f2f2f2,#fff 40px)}
.choose h2{text-align:center;font-weight:300;color:var(--blue);font-size:19px;margin-top:20px}
.choose-grid{display:grid;grid-template-columns:313px 300px;margin:14px 0 0 40px;row-gap:8px}
.choose-grid div{font-family:'Open Sans',sans-serif;font-size:12px;color:#333;display:flex;align-items:center;gap:10px;height:18px}
.arrow{width:0;height:0;border-left:4px solid var(--orange);border-top:4px solid transparent;border-bottom:4px solid transparent}
.news{position:absolute;left:815px;top:638px;width:226px;height:390px;background:var(--panel);padding:10px 10px 0 12px;font-family:'Open Sans',sans-serif}
.news h2{font-family:'Roboto',sans-serif;font-weight:300;color:var(--orange);font-size:21px;line-height:26px}
.news-item h3{font-weight:400;font-size:13px;line-height:14px;color:#444;margin-top:10px}
.news-item time{display:block;font-size:11px;line-height:14px;color:#777;margin-top:3px}
.news-item p{font-size:11px;line-height:19px;color:#222;margin-top:2px}
.news-item a{display:block;font-size:11px;line-height:16px;color:var(--link)}
.news-item:first-of-type{padding-bottom:5px;border-bottom:1px dotted #aaa}
.news-item+.news-item h3{margin-top:11px}
.footer{position:absolute;left:0;top:1081px;width:1120px;height:119px;background:var(--blue)}
.footer-band{position:absolute;left:80px;top:0;width:960px;height:6px;background:var(--orange)}
.footer-nav{position:absolute;left:80px;top:29px;color:#fff;font-size:14px;font-weight:400;display:flex;gap:9px}
.copy{position:absolute;left:80px;top:60px;font-size:11.5px;color:#5a96cf;font-weight:400}
.f-head{color:var(--orange);font-size:14px;font-weight:400}
.f-contact{position:absolute;left:692px;top:29px;color:#fff;font-size:14px;font-weight:400}
.f-contact div{display:flex;align-items:center;gap:6px;margin-top:7px}
.f-follow{position:absolute;left:939px;top:29px}
.socials{display:flex;gap:5px;margin-top:9px}
.socials span{width:26px;height:26px;border-radius:50%;background:#fff;border:2px solid #d8d8d8}
</style>
</head>
<body>
<div class="topbar"><div class="topbar-inner">
  <span><svg width="12" height="9" viewBox="0 0 12 9"><rect width="12" height="9" rx="1" fill="#fff"/><path d="M0 1l6 4 6-4" stroke="#e3a33a" fill="none"/></svg>info@harbincoinage.example</span>
  <span><svg width="7" height="12" viewBox="0 0 7 12"><rect x=".5" y=".5" width="6" height="11" rx="1" fill="none" stroke="#fff"/><circle cx="3.5" cy="9.5" r=".8" fill="#fff"/></svg>+12 40213 78650</span>
</div></div>

<header class="header">
  <div class="brand"><span class="brand-mark"></span><span class="brand-name">HARBIN COINAGE</span></div>
  <div class="brand-tag">INTERNATIONAL MONEY TRANSFER</div>
  <nav class="nav"><a class="active" href="#">Home</a><a href="#">Services</a><a href="#">Transfer</a><a href="#">About us</a><a href="#">Contact us</a><a href="#">FAQ</a></nav>
</header>

<section class="hero">
  <div class="hero-photo" role="img" aria-label="Photo of a modern glass office building with a curved roof, warm orange tones"></div>
  <div class="hero-edge"></div>
  <div class="hero-panel"></div>
  <div class="hero-copy">
    <h1>INTERNATIONAL<br>MONEY TRANSFER</h1>
    <p>We do cash exchange and international money transfers to bank accounts all over the world</p>
  </div>
</section>

<p class="intro">Curabitur vel diam in massa porttitor dictum id in lorem. Vivamus faucibus ac leo ac dignissim. Maecenas orci est, euismod facilisis feugiat sit amet, semper ut tortor. Donec eleifend accumsan nisl, nec laoreet leo iaculis sit amet. Vivamus varius arcu eu sagittis aliquam. Vivamus accumsan cursus hendrerit.</p>
<div class="rule"></div>

<aside class="promo">
  <span class="promo-upto">upto</span>
  <span class="promo-pct">20<span class="stack"><span>%</span><span>off</span></span></span>
  <span class="promo-label">ON MONEY<br>TRANSFER ›</span>
  <div class="promo-globe" role="img" aria-label="Globe illustration showing the Americas"></div>
  <div class="promo-corner"><span>KNOW<br>MORE</span></div>
</aside>

<section class="col col-who">
  <svg class="col-icon" viewBox="0 0 32 32"><circle cx="16" cy="16" r="15" fill="none" stroke="#1d5489" stroke-width="1.5"/><circle cx="15" cy="17" r="8" fill="none" stroke="#1d5489" stroke-width="1.5"/><path d="M7 17h16M15 9v16M9 13h12M9 21h12" stroke="#1d5489" fill="none"/></svg>
  <h2>WHO WE ARE</h2>
  <p>Nam vulputate mauris id arcu pharetra, sed posuere quam cursus. Nullam eget massa vel mi posuere venenatis sed quis tortor. In hac habitasse platea dictumst.</p>
  <p>Fusce nisi tellus, fermentum a luctus eget, convallis vitae orci. In commodo egestas magna quis placerat. Quisque adipiscing consequat nisi, nec accumsan quam venenatis ac.</p>
</section>
<div class="col-divider"></div>
<section class="col col-what">
  <svg class="col-icon" viewBox="0 0 32 32"><circle cx="16" cy="16" r="15" fill="none" stroke="#1d5489" stroke-width="1.5"/><path d="M10 23l8-8" stroke="#1d5489" stroke-width="3" stroke-linecap="round"/><circle cx="20" cy="12" r="4" fill="#1d5489"/><circle cx="21.5" cy="10.5" r="1.6" fill="#fff"/></svg>
  <h2>WHAT WE DO</h2>
  <p>Nam vulputate mauris id arcu pharetra, sed posuere quam cursus.</p>
  <ul class="checks">
    <li><svg width="10" height="10" viewBox="0 0 10 10"><circle cx="5" cy="5" r="5" fill="#f39c1f"/><path d="M2.6 5.1l1.7 1.6 3.1-3.2" stroke="#fff" stroke-width="1.3" fill="none"/></svg>Nullam eget massa vel mi posuere</li>
    <li><svg width="10" height="10" viewBox="0 0 10 10"><circle cx="5" cy="5" r="5" fill="#f39c1f"/><path d="M2.6 5.1l1.7 1.6 3.1-3.2" stroke="#fff" stroke-width="1.3" fill="none"/></svg>Venenatis sed quis tortor</li>
    <li><svg width="10" height="10" viewBox="0 0 10 10"><circle cx="5" cy="5" r="5" fill="#f39c1f"/><path d="M2.6 5.1l1.7 1.6 3.1-3.2" stroke="#fff" stroke-width="1.3" fill="none"/></svg>In hac habitasse platea dictumst.</li>
    <li><svg width="10" height="10" viewBox="0 0 10 10"><circle cx="5" cy="5" r="5" fill="#f39c1f"/><path d="M2.6 5.1l1.7 1.6 3.1-3.2" stroke="#fff" stroke-width="1.3" fill="none"/></svg>Fusce nisi tellus fermentum a luctus</li>
    <li><svg width="10" height="10" viewBox="0 0 10 10"><circle cx="5" cy="5" r="5" fill="#f39c1f"/><path d="M2.6 5.1l1.7 1.6 3.1-3.2" stroke="#fff" stroke-width="1.3" fill="none"/></svg>In commodo egestas magna quis</li>
  </ul>
</section>

<section class="choose">
  <h2>WHY SHOULD YOU CHOOSE US</h2>
  <div class="choose-grid">
    <div><i class="arrow"></i>Cras accumsan orci mauris ut aliquam</div>
    <div><i class="arrow"></i>Cras accumsan orci mauris ut aliquam</div>
    <div><i class="arrow"></i>Ipsum Fusce quam dui accumsan a magna</div>
    <div><i class="arrow"></i>Ipsum Fusce quam dui accumsan a magna</div>
    <div><i class="arrow"></i>Faucibus Vestibulum sapien leo</div>
    <div><i class="arrow"></i>Faucibus Vestibulum sapien leo</div>
  </div>
</section>

<aside class="news">
  <h2>NEWS &amp; EVENTS</h2>
  <article class="news-item">
    <h3>Vestibulum lacinia congue commodo</h3>
    <time>November 10, 2013</time>
    <p>Sed ullamcorper enim quis dolor pellentesque dictum. Integer convallis, massa tincidunt laoreet auctor, mi ante pretium lacus, ac congue odio ante non nunc....</p>
    <a href="#">Read More ›</a>
  </article>
  <article class="news-item">
    <h3>Praesent cursus lacus ac eros</h3>
    <time>November 9, 2013</time>
    <p>Sed ullamcorper enim quis dolor pellentesque dictum. Integer convallis, massa tincidunt laoreet auctor, mi ante pretium lacus, ac congue odio ante non nunc....</p>
    <a href="#">Read More ›</a>
  </article>
</aside>

<footer class="footer">
  <div class="footer-band"></div>
  <nav class="footer-nav"><a href="#">Home</a>|<a href="#">Services</a>|<a href="#">Transfer</a>|<a href="#">About us</a>|<a href="#">Contact us</a>|<a href="#">FAQ</a></nav>
  <div class="copy">Copyright © 2013 Harbin Coinage. All rights reserved</div>
  <div class="f-contact">
    <div class="f-head">Contact us</div>
    <div><svg width="13" height="10" viewBox="0 0 13 10"><rect width="13" height="10" rx="1" fill="#ccc"/><path d="M0 1l6.5 4.5L13 1" stroke="#1d5489" fill="none"/></svg>info@harbincoinage.example</div>
    <div><svg width="8" height="13" viewBox="0 0 8 13"><rect x=".5" y=".5" width="7" height="12" rx="1" fill="none" stroke="#ccc"/><circle cx="4" cy="10.5" r=".9" fill="#ccc"/></svg>+12 40213 78650</div>
  </div>
  <div class="f-follow">
    <div class="f-head">Follow us on</div>
    <div class="socials"><span></span><span></span><span></span></div>
  </div>
</footer>
</body>
</html>
```